For Lease Sign to Attract National Retail Tenants

Attached is a logo design that was created by Pixel Harbor. I will like to develop a leasing sign that is 4 foot wide by 4 foot high or 4 feet wide and 6 feet high. I would like the sign to have a black background and use the colors that are in the logo. These will be signs that are placed in front of shopping centers and are often read by passing motorist so the sign must be simple, clean, very easy to read, distinctive, and have as few words as possible. It would be good if small amounts of bright green can be added as a boarder or ????? The text should be FOR LEASE, 555-283-7716, Wade Hollins. I will want to also design cards and letter head around the same theme.

Target Market(s)

National retail tenants wanting to lease space in my shopping centers

Industry/Entity Type

Real Estate Development

Contact Information for Business Card

Tern Holdings KR, LLC Wade Hollins President & CEO 4127 Orvell Ave. Suite 308 La Jolla, CA 92037 555-283-7716 wadehollins@mailvexa.example

```html
<!DOCTYPE html>
<html lang="en">
<head>
<meta charset="utf-8">
<title>Tern Holdings KR — Lease Sign &amp; Stationery</title>
<link rel="stylesheet" href="https://fonts.googleapis.com/css2?family=Roboto+Condensed:wght@400;700&family=Open+Sans:wght@400;600;700&display=swap">
<style>
  :root {
    --ink: #111111;
    --charcoal: #231f1e;
    --red: #ee2b36;
    --green: #7dc242;
    --band-grey: #d4d4d4;
    --phone-grey: #e3e3e3;
    --paper: #ffffff;
    --cream: #f1ede2;
    --page: #efefef;
    --stage: #e4e4e4;
    --muted: #8a8a8a;
  }
  * { box-sizing: border-box; margin: 0; padding: 0; }
  html, body { width: 877px; height: 1200px; overflow: hidden; }
  body { background: var(--page); font-family: "Open Sans", sans-serif; position: relative; }

  .brand { display: inline-flex; align-items: center; gap: 7px; font-family: "Roboto Condensed", sans-serif; font-weight: 700; letter-spacing: .06em; text-transform: uppercase; white-space: nowrap; }
  .brand__mark { width: 9px; height: 9px; background: var(--red); flex: none; }
  .brand--light { color: #e8e8e8; }
  .brand--dark { color: var(--ink); }

  /* Lease sign */
  .sign-zone { position: absolute; left: 0; top: 0; width: 877px; height: 360px; }
  .lease-sign { position: absolute; left: 296px; top: 38px; width: 285px; height: 285px; background: var(--ink); display: flex; flex-direction: column; font-family: "Roboto Condensed", sans-serif; }
  .lease-sign__rule { height: 6px; background: var(--green); flex: none; }
  .lease-sign__logo { height: 94px; display: flex; align-items: center; justify-content: center; }
  .lease-sign__logo .brand { font-size: 17px; }
  .lease-sign__gap { height: 6px; flex: none; }
  .lease-sign__headline { height: 65px; background: var(--band-grey); color: var(--red); font-weight: 700; font-size: 58px; line-height: 65px; text-align: center; letter-spacing: -.01em; }
  .lease-sign__phone { color: var(--phone-grey); font-weight: 700; font-size: 45px; text-align: center; line-height: 1; margin-top: 9px; letter-spacing: -.01em; }
  .lease-sign__name { color: var(--red); font-weight: 700; font-size: 27px; text-align: center; line-height: 1; margin-top: 7px; }
  .lease-sign__foot { margin-top: auto; }
  .lease-sign__foot .lease-sign__rule { margin-bottom: 4px; }

  /* Business cards */
  .card-zone { position: absolute; left: 0; top: 360px; width: 877px; height: 240px; background: var(--stage); }
  .card { position: absolute; top: 45px; width: 255px; height: 150px; box-shadow: 0 4px 12px rgba(0,0,0,.18); }
  .card--back { background: var(--charcoal); display: flex; align-items: center; justify-content: center; }
  .card--back .brand { font-size: 17px; }
  .card--front { background: var(--cream); padding: 16px 20px; }
  .card--front .brand { position: absolute; right: 16px; bottom: 12px; font-size: 11px; gap: 6px; }
  .card--front .brand__mark { width: 7px; height: 7px; }
  .card__name { font-weight: 700; font-size: 14px; line-height: 1.35; color: var(--ink); }
  .card__role { font-size: 10px; line-height: 1.35; color: var(--red); margin-bottom: 7px; }
  .card__line { font-size: 9.5px; color: #333; line-height: 1.35; }

  /* Stationery */
  .stationery-zone { position: absolute; left: 0; top: 600px; width: 877px; height: 600px; background: var(--page); }
  .folder { position: absolute; left: 70px; top: 50px; width: 280px; height: 380px; background: var(--charcoal); box-shadow: 0 6px 16px rgba(0,0,0,.22); display: flex; align-items: flex-end; justify-content: center; padding-bottom: 60px; }
  .folder .brand { font-size: 16px; }
  .letterhead { position: absolute; left: 385px; top: 30px; width: 300px; height: 390px; background: var(--paper); box-shadow: 0 6px 16px rgba(0,0,0,.14); padding: 26px 28px; font-size: 8px; color: #555; line-height: 1.55; }
  .letterhead .brand { font-size: 12px; margin-bottom: 28px; }
  .letterhead p { margin-bottom: 9px; }
  .letterhead__sign { margin-top: 20px; color: var(--ink); font-weight: 600; }
  .letterhead__foot { position: absolute; left: 28px; right: 28px; bottom: 20px; border-top: 1px solid #ddd; padding-top: 7px; font-size: 7px; color: var(--muted); display: flex; justify-content: space-between; gap: 10px; white-space: nowrap; }
  .envelope { position: absolute; left: 520px; top: 440px; width: 300px; height: 140px; background: var(--paper); box-shadow: 0 6px 16px rgba(0,0,0,.16); padding: 18px 20px; }
  .envelope .brand { font-size: 11px; }
  .envelope__address { position: absolute; left: 20px; top: 40px; font-size: 7.5px; color: var(--muted); line-height: 1.5; }
  .envelope__stripe { position: absolute; left: 0; right: 0; bottom: 0; height: 5px; background: var(--red); }
</style>
</head>
<body>
  <section class="sign-zone">
    <div class="lease-sign">
      <div class="lease-sign__rule"></div>
      <div class="lease-sign__logo"><span class="brand brand--light"><span class="brand__mark"></span>Tern Holdings KR</span></div>
      <div class="lease-sign__rule"></div>
      <div class="lease-sign__gap"></div>
      <div class="lease-sign__headline">FOR LEASE</div>
      <div class="lease-sign__phone">555-283-7716</div>
      <div class="lease-sign__name">Wade Hollins</div>
      <div class="lease-sign__foot"><div class="lease-sign__rule"></div></div>
    </div>
  </section>

  <section class="card-zone">
    <div class="card card--back" style="left:40px"><span class="brand brand--light"><span class="brand__mark"></span>Tern Holdings KR</span></div>
    <div class="card card--front" style="left:311px">
      <div class="card__name">Name Surname</div>
      <div class="card__role">Manager Director</div>
      <div class="card__line">48 Fenwick Road</div>
      <div class="card__line">Marlow, IA 52031</div>
      <div class="card__line">+00 0000 0000</div>
      <div class="card__line">contact@example.com</div>
      <span class="brand brand--dark"><span class="brand__mark"></span>Tern Holdings KR</span>
    </div>
    <div class="card card--back" style="left:582px"><span class="brand brand--light"><span class="brand__mark"></span>Tern Holdings KR</span></div>
  </section>

  <section class="stationery-zone">
    <div class="folder"><span class="brand brand--light"><span class="brand__mark"></span>Tern Holdings KR</span></div>
    <div class="letterhead">
      <span class="brand brand--dark"><span class="brand__mark"></span>Tern Holdings KR</span>
      <p>Dear Client,</p>
      <p>Thank you for your interest in our retail centers. We look forward to working with you on your next location.</p>
      <p>Please review the enclosed terms and contact our office with any questions.</p>
      <p class="letterhead__sign">Sincerely,<br>Wade Hollins</p>
      <div class="letterhead__foot"><span>4127 Orvell Ave. Suite 308, La Jolla, CA 92037</span><span>555-283-7716</span></div>
    </div>
    <div class="envelope">
      <span class="brand brand--dark"><span class="brand__mark"></span>Tern Holdings KR</span>
      <div class="envelope__address">4127 Orvell Ave. Suite 308<br>La Jolla, CA 92037</div>
      <div class="envelope__stripe"></div>
    </div>
  </section>
</body>
</html>
```